Brightwell Capital - fund management and algorithmic design

We're looking for a web design for a new company called brightwell capital which is based out of London.

The photography provided will be a major part of the creative content. The intent is to have a sharp, clear, professional, slick look. Less is more and clutter is not the root that should be followed.

A logo has been selected and the photography provided will give the designer a good idea of what we are looking for. The logo designer is still getting back to me with the very final version but what is provided is good enough to move forward with. the final design will likely have this changed slightly.

The photos are about 1.2 meg each at 86 pdi. I believe this is about right for a high quality web image.

At some point on the site it should have: Integrity, Innovative, Progressive. These are core principles of the company. Also ,Fund management and algorithmic design could be used somewhere as this explains exactly what we do.

I also wish to have the secondary pages designed too. However, rather than asking everybody to do this i will ask a select few designers to look at one of the pages. The chosen designer will then be asked to finish the other pages too. These are expected to be quite simple, nothing fussy - clean and presentable with a small amount of room for artistic license.

Also the links to these two sites will give you a very good idea of what we're looking for.

quendor.com
tavelpointrix.com
birchwardlanefx.com
Updates

Hi,

sorry for as i had problem getting the final images from the photographer as he's been away and busy.

However, we now the the logo (be it not the very final version) and the photos uploaded.  Please read the brief again as this has been updated too.

Initially i'd be happy if you made up the front page and after that i will ask a small handful of designers to submit a design for the secondary page - this way i feel is better as it uses less of your time.  These pages are likely to use the photography for a backdrop too.

Looking forward to your designs.

Regards,

Dominic

Reason: I have extended the deadline as the first week has been held up because of delays in content. thanks, Dominic

Target Market(s)

wealth individuals who wish to diversify their investment portfolios with investments predominantly in the foreign exchange markets as well as some financial products offered by ZPLHoldings.com

Industry/Entity Type

It Company

Requirements
Must have
• There are three photos that the site must use, once the final design is fully operational and coded we want the first three photos to rotate on the front page. Much like quendorr.com

An area where a prospective client can enter their email address to receive market new letters and correspondences from brightwell capital.

front page

about us,
managed accounts
systems and performance

```html
<!DOCTYPE html>
<html lang="en">
<head>
<meta charset="utf-8">
<title>Brightwell Capital – Fund management and algorithmic design</title>
<link rel="stylesheet" href="https://fonts.googleapis.com/css2?family=Arimo:wght@400;700&family=Noto+Sans:wght@400;500&display=swap">
<style>
  :root {
    --teal: #47a8bd;
    --teal-light: #5ab6c9;
    --page-bg: #ececec;
    --white: #ffffff;
    --ink: #2b2b2b;
    --body-text: #6a6a6a;
    --rule: #d2d2d2;
    --icon-grey: #58595b;
    --footer: #363638;
    --footer-base: #2c2c2e;
    --footer-text: #c9c9c9;
    --divider-dark: #4d4d50;
    --field-bg: #f4f4f4;
  }
  * { margin: 0; padding: 0; box-sizing: border-box; }
  html, body { width: 929px; height: 1200px; overflow: hidden; }
  body {
    background: var(--page-bg);
    font-family: "Arimo", Arial, sans-serif;
    color: var(--body-text);
    position: relative;
  }
  .top-strip { position: absolute; top: 0; left: 0; width: 929px; height: 5px; background: #3a3a3a; }
  .page {
    position: absolute; left: 53px; top: 5px; width: 827px; height: 1195px;
    background: var(--white);
    box-shadow: 0 0 6px rgba(0,0,0,.25);
  }
  .abs { position: absolute; }

  .brand { left: 68px; top: 24px; font-family: "Noto Sans", sans-serif; font-size: 44px; color: var(--teal); letter-spacing: 2px; line-height: 1; }
  .header-touch { left: 686px; top: 42px; font-size: 12px; color: var(--teal); }
  .social-dot { width: 27px; height: 27px; border-radius: 50%; background: var(--icon-grey); }

  .main-nav { left: 53px; top: 94px; width: 827px; height: 33px; background: var(--teal); }
  .main-nav a { position: absolute; top: 9px; color: var(--white); text-decoration: none; font-size: 13px; }

  .hero { left: 65px; top: 143px; width: 799px; height: 311px;
    background: linear-gradient(160deg, #1c1a1d 0%, #3b3638 40%, #6e6a6e 55%, #2a2527 75%, #121012 100%); }
  .hero-pager { width: 17px; height: 17px; background: var(--white); color: #333; font-size: 11px; text-align: center; line-height: 17px; }
  .hero-pager.is-active { background: #6a6a6a; color: var(--white); }

  .section-title { font-family: "Noto Sans", sans-serif; color: var(--ink); font-weight: 400; }
  .about-title { left: 85px; top: 477px; font-size: 26px; }
  .about-copy { left: 85px; top: 520px; width: 773px; font-size: 11px; line-height: 15px; }
  .read-more { color: var(--teal); font-size: 13px; text-decoration: none; }
  .about-rule { left: 86px; top: 619px; width: 771px; height: 1px; background: var(--rule); }

  .col-divider { top: 658px; width: 1px; height: 222px; background: var(--rule); }
  .feature-title { font-size: 19px; top: 664px; }
  .feature-copy { top: 711px; width: 240px; font-size: 11px; line-height: 16.5px; }
  .feature-copy p + p { margin-top: 16.5px; }

  .site-footer { left: 50px; top: 919px; width: 830px; height: 235px; background: var(--footer); }
  .footer-base { left: 50px; top: 1154px; width: 830px; height: 46px; background: var(--footer-base); }
  .map { left: 67px; top: 971px; width: 184px; height: 135px; background: linear-gradient(135deg, #c9cdb5, #d9d6c4 50%, #b8c3a6); }
  .footer-heading { color: var(--teal-light); font-size: 15px; line-height: 16px; }
  .footer-text { color: var(--footer-text); font-size: 11px; line-height: 17px; }
  .footer-divider { top: 974px; width: 1px; height: 152px; background: var(--divider-dark); }

  .newsletter-field {
    left: 490px; top: 1044px; width: 130px; height: 24px;
    background: var(--field-bg); border: 1px solid #bdbdbd; border-radius: 2px;
    font-family: "Arimo", Arial, sans-serif; font-size: 11px; color: #555; padding: 0 7px;
  }
  .newsletter-field::placeholder { color: #8a8a8a; }
  .newsletter-button {
    left: 490px; top: 1076px; width: 130px; height: 30px;
    background: linear-gradient(#6fb8c8, #4f9fb1); color: var(--white);
    font-family: "Arimo", Arial, sans-serif; font-size: 13px; text-align: center; line-height: 30px;
    border: 0; border-radius: 2px;
  }
  .footer-dot { width: 27px; height: 27px; border-radius: 50%; background: #d7d7d7; }
  .copyright { left: 67px; top: 1171px; color: var(--footer-text); font-size: 11px; }
</style>
</head>
<body>
  <div class="top-strip"></div>
  <div class="page"></div>

  <header>
    <div class="abs brand">LOGO</div>
    <div class="abs header-touch">Get in Touch</div>
    <span class="abs social-dot" style="left:767px;top:35px"></span>
    <span class="abs social-dot" style="left:804px;top:35px"></span>
    <span class="abs social-dot" style="left:840px;top:35px"></span>
  </header>

  <nav class="abs main-nav">
    <a style="left:13px">Home</a>
    <a style="left:74px">About us</a>
    <a style="left:153px">Financials</a>
    <a style="left:239px">Intelligence</a>
    <a style="left:335px">Technology</a>
    <a style="left:429px">Contact</a>
  </nav>

  <div class="abs hero" role="img" aria-label="Night photograph of a lit bridge with gothic towers over the river in London"></div>
  <span class="abs hero-pager" style="left:770px;top:428px">1</span>
  <span class="abs hero-pager" style="left:797px;top:428px">2</span>
  <span class="abs hero-pager" style="left:823px;top:428px">3</span>
  <span class="abs hero-pager is-active" style="left:850px;top:428px">4</span>

  <section>
    <h1 class="abs section-title about-title">About us</h1>
    <p class="abs about-copy">Lorem ipsum dolor sit amet, consectetur adipisicing elit, sed do eiusmod tempor incididunt ut labore et dolore magna aliqua. Ut enim ad minim veniam, quis nostrud exercitation ullamco laboris nisi ut aliquip ex ea commodo consequat. Duis aute irure dolor in reprehenderit in voluptate velit esse cillum dolore eu fugiat nulla pariatur. Excepteur sint occaecat cupidatat non proident, sunt in culpa qui officia deserunt mollit anim id est laborum.</p>
    <a class="abs read-more" style="left:85px;top:572px">Read More &gt;&gt;</a>
    <div class="abs about-rule"></div>
  </section>

  <section class="features">
    <svg class="abs" style="left:76px;top:651px" width="44" height="44" viewBox="0 0 44 44" aria-hidden="true">
      <circle cx="22" cy="22" r="20" fill="none" stroke="#58595b" stroke-width="2"/>
      <rect x="11" y="15" width="22" height="15" rx="1" fill="#47a8bd"/>
      <rect x="18" y="12" width="8" height="4" fill="#47a8bd"/>
      <circle cx="17" cy="21" r="2.5" fill="#fff"/>
      <rect x="22" y="19" width="8" height="1.6" fill="#fff"/>
      <rect x="22" y="23" width="8" height="1.6" fill="#fff"/>
      <rect x="14" y="25" width="6" height="2" fill="#fff"/>
    </svg>
    <h2 class="abs section-title feature-title" style="left:136px">Managed Accounts</h2>

    <svg class="abs" style="left:344px;top:651px" width="44" height="44" viewBox="0 0 44 44" aria-hidden="true">
      <circle cx="22" cy="22" r="21" fill="#58595b"/>
      <g fill="#fff">
        <circle cx="22" cy="22" r="8"/>
        <rect x="20" y="9" width="4" height="26"/>
        <rect x="9" y="20" width="26" height="4"/>
        <rect x="20" y="9" width="4" height="26" transform="rotate(45 22 22)"/>
        <rect x="20" y="9" width="4" height="26" transform="rotate(-45 22 22)"/>
      </g>
      <circle cx="22" cy="22" r="3.5" fill="#58595b"/>
    </svg>
    <h2 class="abs section-title feature-title" style="left:407px">Systems</h2>

    <svg class="abs" style="left:616px;top:651px" width="44" height="44" viewBox="0 0 44 44" aria-hidden="true">
      <circle cx="22" cy="22" r="21" fill="#58595b"/>
      <g fill="#fff">
        <circle cx="10" cy="22" r="1.6"/><circle cx="12" cy="15" r="1.6"/><circle cx="17" cy="10" r="1.6"/>
        <circle cx="24" cy="9" r="1.6"/><circle cx="31" cy="11" r="1.6"/><circle cx="35" cy="17" r="1.6"/>
      </g>
      <path d="M18 28 L31 17" stroke="#fff" stroke-width="3" stroke-linecap="round"/>
      <circle cx="18" cy="28" r="3" fill="#fff"/>
    </svg>
    <h2 class="abs section-title feature-title" style="left:678px">Performance</h2>

    <div class="abs col-divider" style="left:328px"></div>
    <div class="abs col-divider" style="left:596px"></div>

    <div class="abs feature-copy" style="left:77px">
      <p>Personal portfolios, managed with integrity for every one of our clients.</p>
      <p>Each account is run on your behalf with strict risk limits, clear daily reporting and full transparency. Our managers pair deep market experience with a disciplined process to keep your goals in view.</p>
    </div>
    <div class="abs feature-copy" style="left:344px">
      <p>Innovative trading models, built and tested in-house in London.</p>
      <p>Our algorithmic systems are designed by our own team, tested over years of market data and refined as conditions change, with careful human oversight in the foreign exchange markets.</p>
    </div>
    <div class="abs feature-copy" style="left:617px;top:713px">
      <p>A progressive approach, measured openly against clear benchmarks.</p>
      <p>Returns are reported to clients every month in plain terms. Ongoing research helps us adapt to new markets and products while keeping risk under close and careful control.</p>
    </div>
    <a class="abs read-more" style="left:77px;top:849px">Read More &gt;&gt;</a>
    <a class="abs read-more" style="left:344px;top:849px">Read More &gt;&gt;</a>
    <a class="abs read-more" style="left:617px;top:849px">Read More &gt;&gt;</a>
  </section>

  <footer>
    <div class="abs site-footer"></div>
    <div class="abs map" role="img" aria-label="Street map showing the London office location"></div>
    <div class="abs footer-heading" style="left:262px;top:968px">Contact Information<br>Brightwell Capital</div>
    <div class="abs footer-text" style="left:262px;top:1008px">48 Lindell Row, Suite 4B<br>London EC2V 7QP<br>Phone no.+44(20)7946-0182<br>Email us: info@brightwellcapital.co.uk</div>
    <div class="abs footer-divider" style="left:451px"></div>

    <form class="newsletter" action="#">
      <div class="abs footer-heading" style="left:489px;top:967px">Market Newsletter</div>
      <div class="abs footer-text" style="left:490px;top:1000px;font-size:12px;line-height:14px">Enter your email to receive<br>our market newsletters</div>
      <input class="abs newsletter-field" type="email" placeholder="Your email address" aria-label="Email address">
      <button class="abs newsletter-button" type="submit">Subscribe</button>
    </form>
    <div class="abs footer-divider" style="left:656px"></div>

    <div class="abs footer-heading" style="left:691px;top:967px">Get in Touch</div>
    <span class="abs footer-dot" style="left:692px;top:996px"></span>
    <span class="abs footer-dot" style="left:729px;top:996px"></span>
    <span class="abs footer-dot" style="left:765px;top:996px"></span>
    <div class="abs footer-text" style="left:690px;top:1037px;color:var(--teal-light);font-size:12px">Circle/Chirp/Linkfold/RSS</div>

    <div class="abs footer-base"></div>
    <div class="abs copyright">Copyright 2013 Brightwell Capital. All right reserved</div>
  </footer>
</body>
</html>
```